Business Card Design

we need a business card design and logo for a new cleaning company ,called brightmoor cleaning Service,LLC .we provide cleaning services
Updates

i will also like to include the company's website in the business card   brightmoorcleaningservice.example

Industry/Entity Type

Business

Contact Information for Business Card

Brightmoor Cleaning Service,LLC
Marco Villanueva
Owner
marco@brightmoorcleaningservice.example
Cell 555-318-7462
Office 555-407-2853

```html
<!DOCTYPE html>
<html lang="en">
<head>
<meta charset="utf-8">
<title>Brightmoor Cleaning Service, LLC — Business Card</title>
<link href="https://fonts.googleapis.com/css2?family=Open+Sans:wght@400;600;700;800&display=swap" rel="stylesheet">
<style>
  :root {
    --backdrop: #1d4a6c;
    --card-white: #ffffff;
    --navy: #134a78;
    --sky: #1598cf;
    --brand-navy: #123f6e;
    --text-light: #ffffff;
  }
  * { margin: 0; padding: 0; box-sizing: border-box; }
  html, body {
    width: 1200px;
    height: 845px;
    overflow: hidden;
    background: var(--backdrop);
    font-family: "Open Sans", Arial, sans-serif;
  }
  .card {
    position: absolute;
    left: 100px;
    top: 137px;
    width: 1000px;
    height: 572px;
    border-radius: 40px;
    overflow: hidden;
    background: var(--card-white);
    box-shadow: 0 10px 30px rgba(0,0,0,0.35);
  }
  .card-bands {
    position: absolute;
    inset: 0;
    width: 100%;
    height: 100%;
  }
  .brand {
    position: absolute;
    left: 70px;
    top: 58px;
    display: flex;
    align-items: center;
    gap: 30px;
  }
  .brand-square {
    width: 120px;
    height: 120px;
    border-radius: 14px;
    background: var(--brand-navy);
  }
  .brand-name {
    color: var(--brand-navy);
    font-weight: 700;
    line-height: 1.05;
    text-transform: uppercase;
  }
  .brand-name .line-main {
    display: block;
    font-size: 66px;
    letter-spacing: 2px;
  }
  .brand-name .line-sub {
    display: block;
    font-size: 29px;
    letter-spacing: 5px;
  }
  .tagline {
    position: absolute;
    left: 150px;
    top: 255px;
    height: 32px;
    line-height: 32px;
    white-space: nowrap;
    color: var(--text-light);
    font-weight: 700;
    font-size: 23px;
    letter-spacing: 7px;
    text-transform: uppercase;
    transform: rotate(-1.95deg);
    transform-origin: left center;
  }
  .person {
    position: absolute;
    left: 165px;
    top: 310px;
    color: var(--text-light);
  }
  .person-name {
    font-size: 40px;
    font-weight: 700;
    text-transform: uppercase;
    letter-spacing: 0.5px;
    line-height: 1.1;
  }
  .person-role {
    font-size: 25px;
    font-weight: 600;
    margin-top: 4px;
  }
  .contacts {
    position: absolute;
    left: 165px;
    top: 404px;
    list-style: none;
    color: var(--text-light);
  }
  .contact {
    display: flex;
    align-items: center;
    gap: 44px;
    height: 37px;
    font-size: 27px;
    font-weight: 600;
  }
  .contact-icon {
    width: 22px;
    height: 22px;
    flex: none;
  }
</style>
</head>
<body>
  <main class="card">
    <svg class="card-bands" viewBox="0 0 1000 572" preserveAspectRatio="none" aria-hidden="true">
      <polygon points="0,252 1000,218 1000,572 0,572" fill="var(--sky)"/>
      <polygon points="0,300 1000,266 1000,572 0,572" fill="var(--navy)"/>
    </svg>

    <header class="brand">
      <div class="brand-square"></div>
      <div class="brand-name">
        <span class="line-main">Brightmoor</span>
        <span class="line-sub">Cleaning Service, LLC</span>
      </div>
    </header>

    <p class="tagline">We provide cleaning services</p>

    <section class="person">
      <h1 class="person-name">Marco Villanueva</h1>
      <p class="person-role">Owner</p>
    </section>

    <ul class="contacts">
      <li class="contact">
        <svg class="contact-icon" viewBox="0 0 22 22" aria-label="Cell">
          <rect x="5" y="1" width="12" height="20" rx="2" fill="none" stroke="#fff" stroke-width="2"/>
          <rect x="8" y="4" width="6" height="10" fill="#fff"/>
        </svg>
        <span>555-318-7462</span>
      </li>
      <li class="contact">
        <svg class="contact-icon" viewBox="0 0 22 22" aria-label="Office">
          <path d="M6 2 L9 2 L10 7 L8 9 Q10 14 13 15 L15 13 L20 14 L20 18 Q19 21 15 20 Q4 17 2 6 Q2 2 6 2 Z" fill="#fff"/>
        </svg>
        <span>555-407-2853</span>
      </li>
      <li class="contact">
        <svg class="contact-icon" viewBox="0 0 22 22" aria-label="Email">
          <rect x="1.5" y="4.5" width="19" height="13" fill="none" stroke="#fff" stroke-width="2"/>
          <polyline points="2,5 11,12 20,5" fill="none" stroke="#fff" stroke-width="2"/>
        </svg>
        <span>marco@brightmoorcleaningservice.example</span>
      </li>
      <li class="contact">
        <svg class="contact-icon" viewBox="0 0 22 22" aria-label="Website">
          <circle cx="11" cy="11" r="9" fill="none" stroke="#fff" stroke-width="2"/>
          <ellipse cx="11" cy="11" rx="4" ry="9" fill="none" stroke="#fff" stroke-width="1.5"/>
          <line x1="2" y1="11" x2="20" y2="11" stroke="#fff" stroke-width="1.5"/>
        </svg>
        <span>www.brightmoorcleaningservice.example</span>
      </li>
    </ul>
  </main>
</body>
</html>
```